Bill board design For Marlowe’s Construction

Billboard Design Request
Please design the billboard to match the branding, colors, and overall feel of our website: Marlowe's Construction Website
MARLOWE’S CONSTRUCTION
CONCRETE BUILT FOR GENERATIONS
⭐ 5-Star Rated on Zorvix
Please Include:
* All three attached project photos
* Company logo(s)
* Phone Number: 555-214-7630
* Website: MarlowesConstruction.example
* Zorvix logo with 5-star rating graphic
* Chatterly logo
* Pixtoria logo
Service Area:
Kalamazoo • Battle Creek • Coldwater • Grand Rapids
Please arrange the photos and layout in whatever way creates the strongest visual impact and readability from the road. The company name, headline, phone number, and website should be highly visible at highway speeds.
The overall appearance should be clean, professional, premium, and consistent with our website branding while highlighting our reputation, craftsmanship, and quality concrete work.
People Driving By
Concrete Construction

```html
<!DOCTYPE html>
<html lang="en">
<head>
<meta charset="utf-8">
<title>Marlowe’s Construction Billboard</title>
<link rel="stylesheet" href="https://fonts.googleapis.com/css2?family=Anton&family=Montserrat:wght@600;700;800&display=swap">
<style>
  :root {
    --brand-blue: #1a8be0;
    --band-blue: #1577c9;
    --ink: #0b0b0c;
    --footer: #1c1c1f;
    --white: #f2f2f2;
    --muted: #8a8d92;
    --star: #f6c21a;
  }
  html, body {
    margin: 0;
    width: 1200px;
    height: 1200px;
    overflow: hidden;
    background: #ffffff;
  }
  .billboard {
    position: absolute;
    left: 218px;
    top: 410px;
    width: 763px;
    height: 381px;
    display: block;
  }
  .display { font-family: "Anton", "Oswald", sans-serif; }
  .sans { font-family: "Montserrat", "Arial", sans-serif; }
  .headline { fill: var(--white); font-size: 100px; }
  .tagline { fill: var(--brand-blue); font-size: 50px; }
  .brand-name { fill: var(--brand-blue); font-weight: 800; font-size: 44px; }
  .brand-sub { fill: var(--brand-blue); font-weight: 800; font-size: 16px; letter-spacing: 4px; }
  .rating-name { fill: var(--white); font-weight: 700; font-size: 14px; }
  .rating-text { fill: var(--white); font-weight: 700; font-size: 12px; letter-spacing: 1px; }
  .phone { fill: var(--white); font-weight: 800; font-size: 41px; }
  .web { fill: var(--white); font-weight: 700; font-size: 19px; }
  .social { fill: var(--white); font-weight: 700; font-size: 13px; }
  .areas { fill: var(--white); font-weight: 600; font-size: 13px; letter-spacing: 1.6px; }
</style>
</head>
<body>
<svg class="billboard" viewBox="273 512 954 476" xmlns="http://www.w3.org/2000/svg">
  <defs>
    <linearGradient id="fill-driveway" x1="0" y1="0" x2="0" y2="1">
      <stop offset="0" stop-color="#5f7a3a"/>
      <stop offset="0.45" stop-color="#7a6a58"/>
      <stop offset="1" stop-color="#cdbfae"/>
    </linearGradient>
    <linearGradient id="fill-walkway" x1="0" y1="0" x2="0" y2="1">
      <stop offset="0" stop-color="#5a4636"/>
      <stop offset="1" stop-color="#b5683a"/>
    </linearGradient>
    <linearGradient id="fill-crew" x1="0" y1="0" x2="1" y2="1">
      <stop offset="0" stop-color="#6b7a52"/>
      <stop offset="1" stop-color="#4a3a2c"/>
    </linearGradient>
  </defs>

  <!-- base -->
  <rect x="273" y="512" width="954" height="476" fill="var(--ink)"/>
  <rect x="273" y="512" width="578" height="3" fill="var(--brand-blue)"/>

  <!-- project photos -->
  <polygon role="img" aria-label="Photo: new concrete driveway leading to a brick garage" points="851,512 1227,512 1227,745 779,745" fill="url(#fill-driveway)"/>
  <polygon role="img" aria-label="Photo: stamped orange concrete walkway in front of a house" points="775,752 968,752 915,940 783,940 793,860 740,860" fill="url(#fill-walkway)"/>
  <polygon role="img" aria-label="Photo: crew pouring concrete from a pump hose" points="975,752 1227,752 1227,940 922,940" fill="url(#fill-crew)"/>

  <!-- dividers -->
  <rect x="776" y="745" width="451" height="7" fill="var(--brand-blue)"/>
  <line x1="849" y1="512" x2="740" y2="862" stroke="var(--brand-blue)" stroke-width="4"/>
  <line x1="972" y1="750" x2="918" y2="942" stroke="var(--brand-blue)" stroke-width="5"/>

  <!-- brand -->
  <rect x="330" y="553" width="74" height="74" fill="var(--brand-blue)"/>
  <text class="sans brand-name" x="451" y="604" textLength="324" lengthAdjust="spacingAndGlyphs">MARLOWE’S</text>
  <text class="sans brand-sub" x="452" y="628" textLength="323" lengthAdjust="spacingAndGlyphs">CONSTRUCTION L.L.C</text>
  <line x1="452" y1="637" x2="775" y2="637" stroke="var(--brand-blue)" stroke-width="1.5"/>

  <!-- headline -->
  <text class="display headline" x="312" y="736" textLength="443" lengthAdjust="spacingAndGlyphs">CONCRETE</text>
  <text class="display tagline" x="313" y="786" textLength="437" lengthAdjust="spacingAndGlyphs">BUILT FOR GENERATIONS</text>

  <!-- rating -->
  <rect x="312.5" y="803.5" width="376" height="36" rx="8" fill="none" stroke="#55585d" stroke-width="1.2"/>
  <text class="sans rating-name" x="320" y="827">Zorvix</text>
  <g fill="var(--star)">
    <polygon transform="translate(373 822)" points="0,-8 2.35,-3.24 7.6,-2.47 3.8,1.24 4.7,6.47 0,4 -4.7,6.47 -3.8,1.24 -7.6,-2.47 -2.35,-3.24"/>
    <polygon transform="translate(394 822)" points="0,-8 2.35,-3.24 7.6,-2.47 3.8,1.24 4.7,6.47 0,4 -4.7,6.47 -3.8,1.24 -7.6,-2.47 -2.35,-3.24"/>
    <polygon transform="translate(415 822)" points="0,-8 2.35,-3.24 7.6,-2.47 3.8,1.24 4.7,6.47 0,4 -4.7,6.47 -3.8,1.24 -7.6,-2.47 -2.35,-3.24"/>
    <polygon transform="translate(436 822)" points="0,-8 2.35,-3.24 7.6,-2.47 3.8,1.24 4.7,6.47 0,4 -4.7,6.47 -3.8,1.24 -7.6,-2.47 -2.35,-3.24"/>
    <polygon transform="translate(457 822)" points="0,-8 2.35,-3.24 7.6,-2.47 3.8,1.24 4.7,6.47 0,4 -4.7,6.47 -3.8,1.24 -7.6,-2.47 -2.35,-3.24"/>
  </g>
  <text class="sans rating-text" x="480" y="827" textLength="196" lengthAdjust="spacingAndGlyphs">5-STAR RATED ON ZORVIX</text>

  <!-- contact band -->
  <polygon points="273,860 795,860 785,944 273,944" fill="var(--band-blue)"/>
  <rect x="298" y="873" width="52" height="55" rx="8" fill="var(--ink)"/>
  <path d="M312 886 c2-2 5-2 6 0 l3 6 c1 2 0 4-2 5 l-2 1 c2 5 6 9 11 11 l1-2 c1-2 3-3 5-2 l6 3 c2 1 2 4 0 6 l-3 3 c-3 2-7 2-12-1 c-7-4-13-10-16-17 c-2-5-2-9 0-12 z" fill="var(--white)"/>
  <text class="sans phone" x="362" y="906" textLength="284" lengthAdjust="spacingAndGlyphs">555-214-7630</text>
  <text class="sans web" x="364" y="930" textLength="283" lengthAdjust="spacingAndGlyphs">MarlowesConstruction.example</text>
  <line x1="665" y1="870" x2="665" y2="936" stroke="var(--ink)" stroke-width="2"/>
  <circle cx="687" cy="895" r="5" fill="var(--white)"/>
  <text class="sans social" x="696" y="900">Chatterly</text>
  <text class="sans social" x="681" y="922">Pixtoria</text>

  <!-- service area -->
  <rect x="273" y="944" width="954" height="44" fill="var(--footer)"/>
  <text class="sans areas" x="300" y="972">KALAMAZOO</text>
  <circle cx="413" cy="967" r="2" fill="var(--brand-blue)"/>
  <text class="sans areas" x="426" y="972">BATTLE CREEK</text>
  <circle cx="557" cy="967" r="2" fill="var(--brand-blue)"/>
  <text class="sans areas" x="569" y="972">COLDWATER</text>
  <circle cx="678" cy="967" r="2" fill="var(--brand-blue)"/>
  <text class="sans areas" x="690" y="972">GRAND RAPIDS</text>
</svg>
</body>
</html>
```